Label for a new skin care product

Hello, we are launching a new skin care product. It's a face serum. One product only. I have attached the size requirements and a very general look at what is required. The final result will be a label sticker than gets placed on the bottle.

I have created some (amateur) designs using Canva here: https://www.drafvelo.net/board/QX7tLpWmr2K/hJbnTqzVuRk_-YsDw_4_n/view?utm_content=QX7tLpWmr2K&utm_campaign=boardshare&utm_medium=link2&utm_source=sharebutton

The text is what is required on the label. The design we are seeking is a very simply Wordmark logo with interesting font only. You can see I'm seeking ideas on a colorful design as well as something more ordinary/clinical. The people who will buy this product will be more upper class, well paid, and critical thinkers. Upscale. We don't want too many colors due to printing costs.

Target Market(s)

Female 25-45 years old who are hip and savvy

Requirements
Must have
• wordmark logo

```html
<!DOCTYPE html>
<html lang="en">
<head>
<meta charset="utf-8">
<title>Snail Mucin 96% Power Essence Label</title>
<link rel="stylesheet" href="https://fonts.googleapis.com/css2?family=Noto+Serif:wght@400;500;700&family=Noto+Serif+KR:wght@400&display=swap">
<style>
  :root {
    --backdrop: #e9e8e6;
    --label: #fbfbfb;
    --ink: #262626;
    --ink-soft: #555555;
    --rose: #b08a80;
    --rose-tag: #cfa9a2;
    --wash: #e9dcd6;
    --wash-light: #f3ebe7;
  }
  * { margin: 0; padding: 0; box-sizing: border-box; }
  html, body {
    width: 1200px; height: 1200px; overflow: hidden;
    background: var(--backdrop);
  }
  .label {
    position: absolute;
    left: 340px; top: 140px;
    width: 520px; height: 920px;
    background: var(--label);
    border-radius: 6px;
    box-shadow: 0 2px 10px rgba(0,0,0,0.05);
    overflow: hidden;
    font-family: "Noto Serif", serif;
    color: var(--ink);
  }
  .wash {
    position: absolute;
    left: 30px; top: 150px;
    width: 420px; height: 500px;
    background: radial-gradient(ellipse at 55% 30%, var(--wash) 0%, var(--wash-light) 55%, rgba(243,235,231,0) 75%);
    border-radius: 46% 54% 40% 60% / 30% 36% 64% 70%;
  }
  .botanical {
    position: absolute;
    left: 90px; top: 95px;
    width: 290px; height: 180px;
    background: linear-gradient(160deg, #ffffff 0%, #eeeeee 60%, #dcdcdc 100%);
    border-radius: 40% 50% 45% 55%;
  }
  .brush-marks {
    position: absolute;
    right: 0; top: 640px;
    width: 40px; height: 130px;
    background: linear-gradient(180deg, var(--rose) 0%, rgba(176,138,128,0.5) 100%);
    clip-path: polygon(70% 0, 100% 0, 100% 35%, 30% 100%, 0 100%);
    opacity: 0.75;
  }
  .tagline-kr {
    position: absolute;
    right: 90px; top: 272px;
    font-family: "Noto Serif KR", serif;
    font-size: 22px; font-weight: 400; line-height: 1.2;
    color: var(--ink);
    letter-spacing: 1px;
  }
  .product-name {
    position: absolute;
    left: 0; right: 0; top: 0;
    font-weight: 500;
  }
  .product-name .line {
    position: absolute; left: 0; right: 0;
    text-align: center;
    font-size: 84px; line-height: 1; letter-spacing: 1px;
  }
  .product-name .snail { top: 330px; }
  .product-name .mucin { top: 412px; }
  .product-name .percent { top: 500px; font-size: 80px; font-weight: 700; }
  .type-tag {
    position: absolute;
    left: 120px; top: 602px;
    width: 280px; height: 38px;
    background: var(--rose-tag);
    color: #ffffff;
    font-size: 22px; letter-spacing: 3px;
    text-align: center; line-height: 38px;
  }
  .key-ingredient {
    position: absolute;
    left: 0; right: 0; top: 648px;
    text-align: center;
    font-size: 22px; line-height: 1.2; color: var(--ink-soft);
  }
  .free-from {
    position: absolute;
    left: 0; right: 0; top: 700px;
    text-align: center;
    font-size: 18px; line-height: 1.45;
    color: var(--ink-soft);
  }
  .wordmark {
    position: absolute;
    left: 0; right: 0; top: 790px;
    text-align: center;
    font-size: 56px; font-weight: 700; line-height: 1;
    color: var(--rose);
    letter-spacing: 1px;
  }
</style>
</head>
<body>
  <div class="label">
    <div class="wash" role="img" aria-label="Soft beige watercolour wash"></div>
    <div class="botanical" role="img" aria-label="Line illustration of white hibiscus flowers with leaves"></div>
    <div class="brush-marks" role="img" aria-label="Rose brush stroke marks"></div>
    <p class="tagline-kr" lang="ko">뛰어난 수분 공급</p>
    <h1 class="product-name">
      <span class="line snail">SNAIL</span>
      <span class="line mucin">MUCIN</span>
      <span class="line percent">96%</span>
    </h1>
    <p class="type-tag">POWER ESSENCE</p>
    <p class="key-ingredient">with Gotu Kola</p>
    <p class="free-from">Paraben, Alcohol, Fragrance,<br>Phthalate, and Cruelty Free</p>
    <p class="wordmark">Orla</p>
  </div>
</body>
</html>
```